KRT Earthworks*

we are a construction company specialising in Housing, Water Infrastructure and Roadworks
This is the description I would like to be added to the Flyer. I have
also attached a Picture
Krt Earthworks is a Construction Company specializing in Housing, Roadworks
and Water infrastructure. Krt has established itself firmly in the
Construction industry with branches all through Southern Africa as well
as into Africa.
Krt is committed to giving its Clients efficient and Professional
service at all times, We pride ourselves on our ability to meet
deadlines and exceed expectations. Our aim is to establish Successful
Long lasting relationships with our Client base
Colors
Designer to choose only greyscale colors for use in the design.
Look and feel

```html
<!DOCTYPE html>
<html lang="en">
<head>
<meta charset="utf-8">
<title>KRT Earthworks – Flyer</title>
<link rel="stylesheet" href="https://fonts.googleapis.com/css2?family=Roboto:ital,wght@0,400;0,500;0,700;0,900;1,700&display=swap">
<style>
  :root {
    --page-bg: #e4e4e4;
    --paper: #ffffff;
    --ink: #111111;
    --accent: #4a4a4a;
    --band-top: #262626;
    --band-bottom: #5c5c5c;
    --footer-grey: #7a7a7a;
    --pill-top: #6e6e6e;
    --pill-bottom: #303030;
    --black-band: #0c0c0c;
    --icon-mid: #777777;
    --icon-light: #bdbdbd;
    --icon-dark: #3a3a3a;
    --seal-outer: #a8a8a8;
    --seal-ring: #555555;
    --seal-core: #2a2a2a;
  }
  * { box-sizing: border-box; margin: 0; padding: 0; }
  html, body { width: 1200px; height: 1200px; overflow: hidden; }
  body {
    background: var(--page-bg);
    font-family: "Roboto", Arial, sans-serif;
    position: relative;
  }
  .flyer {
    position: absolute;
    left: 160px; top: 30px;
    width: 880px; height: 1140px;
    background: linear-gradient(to bottom, var(--paper) 0%, var(--paper) 22%, #ededed 40%, #e2e2e2 44%);
    overflow: hidden;
    box-shadow: 0 6px 24px rgba(0,0,0,.18);
  }
  .brand {
    position: absolute; top: 64px; left: 0; width: 100%;
    display: flex; justify-content: center; align-items: center; gap: 18px;
  }
  .brand-mark { width: 40px; height: 40px; background: var(--ink); }
  .brand-name {
    font-weight: 900; font-size: 66px; color: var(--ink);
    letter-spacing: 1px; line-height: 1;
  }
  .intro {
    position: absolute; top: 182px; width: 100%; text-align: center;
    font-weight: 700; font-size: 26px; letter-spacing: 1.6px; color: var(--ink);
  }
  .specialty-rule {
    position: absolute; top: 250px; left: 150px; width: 580px; height: 2px;
    background: linear-gradient(to right, transparent, #222 30%, #222 70%, transparent);
  }
  .specialty-pill {
    position: absolute; top: 227px; left: 282px; width: 316px; height: 46px;
    border-radius: 23px;
    background: linear-gradient(to bottom, var(--pill-top), var(--pill-bottom));
    color: #fff; font-weight: 700; font-size: 31px; text-align: center; line-height: 46px;
  }
  .specialty-pill::before, .specialty-pill::after {
    content: ""; position: absolute; top: 17px; width: 12px; height: 12px;
    border-radius: 50%; background: #111;
  }
  .specialty-pill::before { left: 10px; }
  .specialty-pill::after { right: 10px; }
  .service-icons {
    position: absolute; top: 296px; left: 0; width: 100%;
    display: flex; justify-content: center; gap: 62px;
  }
  .service-icons svg { width: 80px; height: 80px; }
  .services-title {
    position: absolute; top: 400px; width: 100%; text-align: center;
    font-weight: 700; color: var(--accent); font-size: 46px; line-height: 56px;
  }
  .services-title .joiner { color: var(--ink); font-size: 32px; }
  .services-title .line { display: block; }
  .hero-photo {
    position: absolute; top: 501px; left: 0; width: 100%; height: 275px;
    background: linear-gradient(to bottom, #e2e2e2 0%, #bdbdbd 10%, #8a8a8a 20%, #909090 30%, #b8b8b8 55%, #a2a2a2 75%, #858585 100%);
  }
  .about-band {
    position: absolute; top: 775px; left: 0; width: 100%; height: 232px;
    background: linear-gradient(to bottom, var(--band-top), var(--band-bottom));
    color: #fff; text-align: center; padding: 0 30px;
  }
  .about-lead { margin-top: 32px; font-size: 22px; line-height: 28px; }
  .about-body { margin-top: 30px; font-size: 19px; line-height: 24px; }
  .contact-band {
    position: absolute; top: 1007px; left: 0; width: 100%; height: 85px;
    background: var(--black-band);
    display: flex; align-items: center; padding-left: 44px;
    color: #e8e8e8;
  }
  .contact-phone { font-weight: 700; font-style: italic; font-size: 25px; }
  .contact-sep { margin: 0 16px; font-size: 22px; }
  .contact-web { font-weight: 500; font-size: 23px; }
  .footer-band {
    position: absolute; top: 1092px; left: 0; width: 100%; height: 48px;
    background: var(--footer-grey);
  }
  .guarantee-seal { position: absolute; left: 697px; top: 981px; width: 136px; height: 136px; }
</style>
</head>
<body>
  <main class="flyer">
    <header class="brand">
      <span class="brand-mark"></span>
      <span class="brand-name">KRT EARTHWORKS</span>
    </header>

    <p class="intro">KRT EARTHWORKS IS A CONSTRUCTION COMPANY</p>

    <div class="specialty-rule"></div>
    <div class="specialty-pill">SPECIALIZING IN</div>

    <div class="service-icons">
      <svg viewBox="0 0 80 80" aria-label="Housing">
        <polygon points="40,6 76,40 66,40 66,72 14,72 14,40 4,40" fill="var(--icon-mid)"/>
        <rect x="20" y="12" width="8" height="16" fill="var(--icon-mid)"/>
        <rect x="33" y="48" width="14" height="24" fill="#fff"/>
      </svg>
      <svg viewBox="0 0 80 80" aria-label="Roadworks">
        <polygon points="40,6 56,66 24,66" fill="#111"/>
        <rect x="29" y="28" width="22" height="7" fill="#fff"/>
        <rect x="26" y="44" width="28" height="7" fill="#fff"/>
        <rect x="14" y="66" width="52" height="8" fill="#111"/>
      </svg>
      <svg viewBox="0 0 80 80" aria-label="Water infrastructure">
        <g transform="rotate(45 40 40)">
          <rect x="34" y="4" width="12" height="72" rx="3" fill="var(--icon-light)"/>
          <rect x="4" y="34" width="72" height="12" rx="3" fill="var(--icon-light)"/>
          <rect x="30" y="2" width="20" height="6" fill="var(--icon-dark)"/>
          <rect x="30" y="72" width="20" height="6" fill="var(--icon-dark)"/>
          <rect x="2" y="30" width="6" height="20" fill="var(--icon-dark)"/>
          <rect x="72" y="30" width="6" height="20" fill="var(--icon-dark)"/>
        </g>
        <circle cx="40" cy="40" r="11" fill="none" stroke="var(--icon-dark)" stroke-width="4"/>
      </svg>
    </div>

    <h1 class="services-title">
      <span class="line">HOUSING, ROADWORKS</span>
      <span class="line"><span class="joiner">AND</span> WATER INFRASTRUCTURE.</span>
    </h1>

    <div class="hero-photo" role="img" aria-label="Photograph of a completed housing development with rows of small homes, power lines and hills behind"></div>

    <section class="about-band">
      <p class="about-lead">Krt has established itself firmly in the Construction industry with branches<br>all through Southern Africa as well as into Africa.</p>
      <p class="about-body">Krt is committed to giving its Clients efficient and Professional service at all times,<br>We pride ourselves on our ability to meet deadlines and exceed expectations.<br>Our aim is to establish Successful Long lasting relationships with our Client base</p>
    </section>

    <div class="contact-band">
      <span class="contact-phone">CALL US NOW : 123 456 789</span>
      <span class="contact-sep">|</span>
      <span class="contact-web">WWW.YOURWEBSITE.COM</span>
    </div>
    <div class="footer-band"></div>

    <svg class="guarantee-seal" viewBox="0 0 136 136" role="img" aria-label="Guarantee seal">
      <circle cx="68" cy="68" r="66" fill="var(--seal-outer)"/>
      <circle cx="68" cy="68" r="58" fill="none" stroke="var(--seal-ring)" stroke-width="3"/>
      <circle cx="68" cy="68" r="38" fill="var(--seal-core)" stroke="var(--seal-outer)" stroke-width="3"/>
    </svg>
  </main>
</body>
</html>
```